Copper Ridge Garage Door Sales & Repair needs a Business Card Design

I need a business card design to go with our new business logo that was created a few months ago.

Copper Ridge Garage Door specializes in selling and installing new garage doors, and new garage door openers. We also take care of all repairs to existing garage doors and garage door openers. All makes and models.

Target Market(s)

Home-owners, renters, anyone who lives in a house and has a garage. Residential and commercial garages.

Industry/Entity Type

Home Improvement

Contact Information for Business Card

I would like the business cards to have rounded corners and be double-sided. My old logo is still on my website at www.copperridgegarage.example. If I was going to incorporate a secondary color on the business cards, I think that orange is a good choice (especially since blue and orange are the colors of our Tulsa Kestrels), but I'm not opposed to seeing a different color if another color works better with my logo colors. I have two logo colors. One designed for a white background and one designed for a darker background. I'm not opposed to using both. Maybe a dark background with the white logo on one side, and a white background with the other logo color on the other side.

My business is a small, locally owned business that I am trying to grow. But I would like my business cards to look very professional. Like we have been in business for a long time. I like traditional to modern looking cards. Just something bold and memorable. My full company name is Copper Ridge Garage Door Sales & Repair. But you can just do COPPER RIDGE GARAGE DOOR, if that works better.

Font styles to use
Serif
Script

Requirements
Must have
• Rounded corners
• Double-sided
• 3-D Elements. Layering of some sort (a sketch of a garage door or a 3rd color (orange) brought in some how. I really like watermarks.
• Matte cards that you can write on.
• White on one side. (Or the lighter blue in my logo). Darker blue logo color on the other side.
• I would like our tag line on the cards somewhere... "For All Your Garage Door Needs".
• I would also like "Call For a FREE Estimate" by the phone number.
• And "Serving the Greater Metro Denver Area" somewhere on the card as well.
Nice to have
• Refer to "Business Card Details" above.

```html
<!DOCTYPE html>
<html lang="en">
<head>
<meta charset="utf-8">
<title>Copper Ridge Garage Doors – Business Card</title>
<link rel="stylesheet" href="https://fonts.googleapis.com/css2?family=Fira+Sans+Condensed:wght@600;700&family=Roboto:ital,wght@0,400;0,500;1,400&display=swap">
<style>
  :root {
    --backdrop: #a8a5a5;
    --navy: #3d4b6d;
    --sky: #aebfd2;
    --white: #ffffff;
    --muted: #55607a;
  }
  * { margin: 0; padding: 0; box-sizing: border-box; }
  html, body { width: 1200px; height: 1200px; overflow: hidden; }
  body { background: var(--backdrop); position: relative; font-family: "Roboto", sans-serif; }

  .card {
    position: absolute;
    left: 215px;
    width: 770px;
    height: 420px;
    border-radius: 24px;
    overflow: hidden;
    background: var(--navy);
  }
  .card--front { top: 118px; }
  .card--back { top: 645px; }

  .brand-name {
    position: absolute;
    font-family: "Fira Sans Condensed", sans-serif;
    font-weight: 700;
    color: var(--white);
    text-transform: uppercase;
    text-align: center;
    line-height: 1.05;
    letter-spacing: 1px;
  }
  .card--front .brand-name { left: 0; right: 0; top: 150px; font-size: 48px; }
  .card--back .brand-name { left: 36px; width: 300px; top: 190px; font-size: 40px; }
  .brand-name small { display: block; font-size: 0.6em; letter-spacing: 4px; margin-top: 6px; }

  .tagline {
    position: absolute;
    left: 0; right: 0; top: 278px;
    text-align: center;
    font-style: italic;
    font-size: 18px;
    color: var(--sky);
    letter-spacing: 0.5px;
  }

  .service-area {
    position: absolute;
    left: 36px; width: 300px; top: 300px;
    text-align: center;
    font-size: 13px;
    color: var(--sky);
    letter-spacing: 0.3px;
  }

  .back-waves { position: absolute; inset: 0; }

  .person { position: absolute; right: 82px; top: 38px; text-align: right; }
  .person__name { font-family: "Fira Sans Condensed", sans-serif; font-weight: 600; font-size: 27px; color: var(--navy); }
  .person__role { font-size: 15px; color: var(--muted); margin-top: 6px; }

  .contact { position: absolute; right: 103px; top: 250px; list-style: none; text-align: right; }
  .contact li { display: flex; align-items: center; justify-content: flex-end; gap: 10px; color: var(--white); font-size: 16.5px; height: 26px; }
  .contact .contact__offer { color: var(--sky); font-weight: 500; font-size: 15px; }
  .contact svg { width: 16px; height: 16px; fill: var(--white); }
  .address { position: absolute; right: 80px; top: 362px; color: var(--white); font-size: 16.5px; }
</style>
</head>
<body>

<section class="card card--front">
  <div class="brand-name">Copper Ridge<small>Garage Doors</small></div>
  <p class="tagline">For All Your Garage Door Needs</p>
</section>

<section class="card card--back">
  <svg class="back-waves" viewBox="0 0 770 420" preserveAspectRatio="none">
    <rect width="770" height="420" fill="var(--sky)"/>
    <path d="M0,42 C110,8 220,20 270,40 C170,30 80,40 0,70 Z" fill="var(--white)"/>
    <path d="M0,62 C170,10 320,40 420,105 C520,165 640,160 770,150 L770,420 L0,420 Z" fill="var(--white)"/>
    <path d="M0,74 C170,30 310,60 410,120 C510,178 640,175 770,166 L770,420 L0,420 Z" fill="var(--navy)"/>
  </svg>

  <div class="person">
    <div class="person__name">Tessa Marlowe</div>
    <div class="person__role">Project Manager</div>
  </div>

  <div class="brand-name">Copper Ridge<small>Garage Doors</small></div>
  <p class="service-area">Serving the Greater Metro Denver Area</p>

  <ul class="contact">
    <li class="contact__offer">Call For a FREE Estimate</li>
    <li>555-014-2290
      <svg viewBox="0 0 16 16" aria-hidden="true"><path d="M2 5c0-2 2-3 6-3s6 1 6 3v1h-3V5H5v1H2zM4 7h8l2 6H2zM6 9h4v2H6z"/></svg>
    </li>
    <li>copperridgegarage.example
      <svg viewBox="0 0 16 16" aria-hidden="true"><path d="M1 3h14v10H1zM2.5 4.5v.4L8 9l5.5-4.1v-.4zM2.5 6.6v5h11v-5L8 10.7z"/></svg>
    </li>
    <li>info@copperridgegarage.example
      <svg viewBox="0 0 16 16" aria-hidden="true"><path d="M8 1a7 7 0 1 0 0 14A7 7 0 0 0 8 1zm0 1.5c.8 0 1.7 1.4 2 3.5H6c.3-2.1 1.2-3.5 2-3.5zM3 6h1.8a12 12 0 0 0 0 4H3a5.5 5.5 0 0 1 0-4zm3 0h4a11 11 0 0 1 0 4H6a11 11 0 0 1 0-4zm5.2 0H13a5.5 5.5 0 0 1 0 4h-1.8a12 12 0 0 0 0-4zM6 11h4c-.3 1.6-1.2 2.5-2 2.5S6.3 12.6 6 11z"/></svg>
    </li>
  </ul>
  <div class="address">4182 Ridgeline Ave Harlow, CO 80000</div>
</section>

</body>
</html>
```